drafting business needs a 2 sided rack card design. Size specificaton

Document Trim Size:
Full Bleed Size (starting document size)
3.86" x 8.39"
When trimmed the Rack cards are 3.74" x 8.27".
300 DPI

I need my logo, product info, and 2 pictures included

This is product information that i need:

- Floor Plans measured to QERT & PLUX standards
- Stunning HD Photography
- Vexolith - your space delivered in perfect 3D
- E &O insured
- Our products delivered next by before 10:00 AM

It also has to my my special offer: Save 50% off Vexolith, Floor Plans, and Photography

My contact info is
www.quillfenstudio.com
dorian@quillfenstudio.com
778-514-0962
Updates

Hey designers, the common element I see in most of the designs that I actually don't like is the use of orange and blue. I think there was some miscommunication. Please Don't use these colors. It really makes the designs Look cheap. I want a clean, high end look.

Target Market(s)

realtors

Industry/Entity Type

Real Estate

Font styles to use
Serif

Colors

Designer to choose colors to be used in the design.

Requirements
Must have
• At least 2 photos and my logo included. it must include all my wording with discount in bold, but classy.
Nice to have
• I want clean classy design. My logo is and 2 photos should be in design. I design should match my logo colors, I think. I have tons of other photos if you think these arent very useful
• Also I have attached a logo from vexolith. Please include this, but smaller than the Quillfen Studio. The Vexolith is just equiptment that I use
Should not have
• This is a discount promotion, but I dont want it to look cheap whatsoever

```html
<!DOCTYPE html>
<html lang="en">
<head>
<meta charset="utf-8">
<title>Quillfen Studio Rack Card</title>
<link href="https://fonts.googleapis.com/css2?family=Lusitana:wght@400;700&family=Libre+Baskerville:wght@400;700&family=Lato:wght@400;700&display=swap" rel="stylesheet">
<style>
  :root{
    --charcoal:#2a2b2e;
    --charcoal-deep:#1c1d1f;
    --gold:#b08d57;
    --gold-deep:#957443;
    --champagne:#e9dfcf;
    --ink:#2b2b2b;
    --panel:#f6f4f0;
    --white:#fff;
    --backdrop:#ebe8e4;
  }
  *{margin:0;padding:0;box-sizing:border-box}
  html,body{width:1200px;height:1200px;overflow:hidden;background:var(--backdrop)}
  .canvas{position:relative;width:1200px;height:1200px}
  .card{position:absolute;top:153px;width:411px;height:894px;background:var(--white);overflow:hidden;box-shadow:0 6px 18px rgba(0,0,0,.18)}
  .card--front{left:118px}
  .card--back{left:670px}

  .brand{position:absolute;top:22px;left:0;width:100%;text-align:center}
  .brand__dot{display:block;width:84px;height:84px;border-radius:50%;background:var(--charcoal);margin:0 auto}
  .brand__name{display:block;margin-top:8px;font-family:"Lusitana",serif;font-weight:400;font-size:34px;color:var(--charcoal);line-height:1}

  .headline-band{position:absolute;top:154px;left:0;width:100%;height:73px;background:linear-gradient(180deg,var(--charcoal),var(--charcoal-deep));color:var(--white);text-align:center;padding-top:6px}
  .headline-band__main{font-family:"Lusitana",serif;font-size:29px;line-height:1.1;display:block}
  .headline-band__sub{font-family:"Lusitana",serif;font-weight:700;font-size:25px;line-height:1.2;display:block;color:var(--champagne)}

  .photo{position:absolute;left:0;width:100%}
  .photo--bedroom{top:227px;height:320px;background:linear-gradient(180deg,#d8cfc8 0%,#c9bcb4 45%,#b9a7a6 70%,#e6ddd8 100%)}
  .photo--living{top:154px;height:320px;background:linear-gradient(180deg,#e9ecef 0%,#cfd4d6 40%,#9c8f7f 75%,#6d5a48 100%)}
  .wave{position:absolute;left:0;width:411px;display:block}

  .inset-photo{position:absolute;left:33px;top:352px;width:140px;height:140px;border-radius:50%;border:5px solid var(--gold);background:linear-gradient(160deg,#d9c7a6,#9b6a45 60%,#e8e2d8)}

  .services__title{position:absolute;top:568px;left:128px;width:156px;height:26px;border-radius:13px;background:var(--charcoal);color:var(--white);font-family:"Libre Baskerville",serif;font-weight:700;font-size:16px;text-align:center;line-height:26px;z-index:2}
  .services{position:absolute;top:582px;left:30px;width:351px;height:198px;background:var(--panel);border-radius:6px}
  .service{position:absolute;width:175px;text-align:center;font-family:"Lato",sans-serif;font-size:13.5px;line-height:1.35;color:var(--ink)}
  .service svg{display:block;margin:0 auto 5px}
  .service--plans{left:0;top:28px}
  .service--3d{left:176px;top:28px}
  .service--photo{left:0;top:122px}
  .service--insured{left:176px;top:122px}

  .offer-lead{position:absolute;top:497px;width:100%;text-align:center;font-family:"Libre Baskerville",serif;font-weight:700}
  .offer-lead__main{display:block;color:var(--charcoal);font-size:19px}
  .offer-lead__time{display:block;color:var(--gold-deep);font-size:16px;margin-top:6px}

  .tag{position:absolute;left:48px;top:546px}

  .partner{position:absolute;top:747px;width:100%;text-align:center;font-family:"Lato",sans-serif;font-weight:700;font-size:28px;color:var(--charcoal);line-height:1}
  .partner__mark{display:inline-block;width:20px;height:20px;background:var(--charcoal);margin-right:7px;vertical-align:-1px}

  .footer{position:absolute;left:0;bottom:0;width:411px;height:114px}
  .footer__call{position:absolute;left:0;width:100%;text-align:center;font-family:"Lato",sans-serif;font-weight:700;color:var(--white);font-size:21px;white-space:nowrap}
  .footer__call svg{vertical-align:-5px;margin:0 4px}
  .footer__phone{color:var(--gold)}
  .footer__contact{position:absolute;left:0;width:100%;text-align:center;font-family:"Lato",sans-serif;font-size:13px;color:var(--white);white-space:nowrap}
  .footer__contact svg{vertical-align:-1px;margin-right:4px}
  .card--front .footer__call{top:44px}
  .card--front .footer__contact{top:79px}
  .card--back .footer__call{top:52px}
  .card--back .footer__contact{top:86px}
</style>
</head>
<body>
<div class="canvas">

  <section class="card card--front">
    <div class="brand"><span class="brand__dot"></span><span class="brand__name">Quillfen Studio</span></div>

    <div class="headline-band">
      <span class="headline-band__main">Floor plans &amp; Photography</span>
      <span class="headline-band__sub">for REALTORS</span>
    </div>

    <div class="photo photo--bedroom" role="img" aria-label="Photograph of a staged bedroom with a made bed, two bedside lamps and a round mirror"></div>
    <svg class="wave" style="top:430px" width="411" height="130" viewBox="0 0 411 130">
      <path d="M0,42 Q205,150 411,60 L411,130 L0,130 Z" fill="var(--white)"/>
      <path d="M0,36 Q205,132 411,36 L411,60 Q205,150 0,42 Z" fill="var(--gold)"/>
      <path d="M0,33 Q205,122 411,26 L411,36 Q205,132 0,36 Z" fill="var(--white)"/>
      <path d="M0,28 Q205,108 411,10 L411,26 Q205,122 0,33 Z" fill="var(--charcoal)"/>
    </svg>

    <div class="services__title">Our Services</div>
    <div class="services">
      <div class="service service--plans">
        <svg width="26" height="26" viewBox="0 0 26 26"><circle cx="13" cy="13" r="12" fill="none" stroke="var(--gold)" stroke-width="1.5"/><rect x="7" y="8" width="12" height="10" fill="none" stroke="var(--gold)" stroke-width="1.3"/><line x1="13" y1="8" x2="13" y2="18" stroke="var(--gold)" stroke-width="1.3"/></svg>
        Floor Plans measured<br>to QERT &amp;<br>PLUX standards
      </div>
      <div class="service service--3d">
        <svg width="26" height="26" viewBox="0 0 26 26"><circle cx="13" cy="13" r="12" fill="none" stroke="var(--gold)" stroke-width="1.5"/><path d="M13,6 L19,9.5 L19,16.5 L13,20 L7,16.5 L7,9.5 Z M7,9.5 L13,13 L19,9.5 M13,13 L13,20" fill="none" stroke="var(--gold)" stroke-width="1.2"/></svg>
        Vexolith-your space<br>delivered in perfect 3D
      </div>
      <div class="service service--photo">
        <svg width="26" height="26" viewBox="0 0 26 26"><circle cx="13" cy="13" r="12" fill="none" stroke="var(--gold)" stroke-width="1.5"/><rect x="6.5" y="8.5" width="13" height="9" rx="1" fill="none" stroke="var(--gold)" stroke-width="1.3"/><circle cx="13" cy="13" r="2.5" fill="none" stroke="var(--gold)" stroke-width="1.2"/></svg>
        Stunning HD<br>Photography
      </div>
      <div class="service service--insured">
        <svg width="26" height="26" viewBox="0 0 26 26"><circle cx="13" cy="13" r="12" fill="none" stroke="var(--gold)" stroke-width="1.5"/><path d="M13,6 L19,8.5 L19,13 Q19,17.5 13,20 Q7,17.5 7,13 L7,8.5 Z" fill="none" stroke="var(--gold)" stroke-width="1.3"/><path d="M10,13 L12.3,15.3 L16,11" fill="none" stroke="var(--gold)" stroke-width="1.3"/></svg>
        <br>E &amp;O insured
      </div>
    </div>

    <div class="footer">
      <svg class="wave" style="top:0" width="411" height="114" viewBox="0 0 411 114">
        <path d="M0,42 Q205,-22 411,42 L411,50 Q205,-12 0,50 Z" fill="var(--gold)"/>
        <path d="M0,55 Q205,-5 411,55 L411,114 L0,114 Z" fill="var(--charcoal)"/>
      </svg>
      <div class="footer__call">CALL TODAY
        <svg width="26" height="26" viewBox="0 0 26 26"><circle cx="13" cy="13" r="11.5" fill="none" stroke="var(--gold)" stroke-width="1.8"/><path d="M9,7.5 L11,7.5 L12,10.5 L10.6,11.6 Q11.8,14.2 14.4,15.4 L15.5,14 L18.5,15 L18.5,17 Q18.5,18.5 17,18.5 Q8,18 7.5,9 Q7.5,7.5 9,7.5 Z" fill="var(--gold)"/></svg>
        <span class="footer__phone">778.514.0962</span></div>
      <div class="footer__contact">
        <svg width="10" height="8" viewBox="0 0 10 8"><rect x="0.5" y="0.5" width="9" height="7" fill="var(--gold)"/><path d="M0.5,0.5 L5,4.5 L9.5,0.5" fill="none" stroke="var(--charcoal)" stroke-width="1"/></svg>dorian@quillfenstudio.com &nbsp;|&nbsp;
        <svg width="10" height="10" viewBox="0 0 10 10"><circle cx="5" cy="5" r="4.3" fill="none" stroke="var(--gold)" stroke-width="1.2"/><line x1="0.7" y1="5" x2="9.3" y2="5" stroke="var(--gold)"/><ellipse cx="5" cy="5" rx="2" ry="4.3" fill="none" stroke="var(--gold)"/></svg>www.quillfenstudio.com
      </div>
    </div>
  </section>

  <section class="card card--back">
    <div class="brand"><span class="brand__dot"></span><span class="brand__name">Quillfen Studio</span></div>

    <div class="photo photo--living" role="img" aria-label="Photograph of a bright living room with large windows, sofas, a rug and a stone fireplace"></div>
    <svg class="wave" style="top:340px" width="411" height="150" viewBox="0 0 411 150">
      <path d="M0,62 Q200,200 411,100 L411,150 L0,150 Z" fill="var(--white)"/>
      <path d="M0,56 Q200,186 411,78 L411,100 Q200,200 0,62 Z" fill="var(--gold)"/>
      <path d="M0,54 Q200,180 411,72 L411,78 Q200,186 0,56 Z" fill="var(--white)"/>
      <path d="M0,44 Q200,165 411,52 L411,72 Q200,180 0,54 Z" fill="var(--charcoal)"/>
    </svg>
    <div class="inset-photo" role="img" aria-label="Photograph of a foyer with a wooden staircase seen from above"></div>

    <div class="offer-lead">
      <span class="offer-lead__main">Our products delivered next</span>
      <span class="offer-lead__time">BY BEFORE 10:00 AM</span>
    </div>

    <svg class="tag" width="320" height="190" viewBox="0 0 320 190">
      <g transform="rotate(-9 170 98)">
        <path d="M62,98 Q30,104 28,130 Q26,150 14,170" fill="none" stroke="#555" stroke-width="2"/>
        <path d="M40,98 L80,45 L300,45 Q308,45 308,53 L308,143 Q308,151 300,151 L80,151 Z" fill="var(--charcoal)"/>
        <circle cx="62" cy="98" r="12" fill="var(--white)" stroke="var(--gold)" stroke-width="3"/>
        <rect x="100" y="55" width="198" height="86" rx="3" fill="var(--white)" stroke="var(--gold)" stroke-width="1.2" stroke-dasharray="3 3"/>
        <text x="199" y="77" text-anchor="middle" font-family="Lato, sans-serif" font-size="15" fill="#333">special offer:</text>
        <text x="199" y="105" text-anchor="middle" font-family="Libre Baskerville, serif" font-weight="700" font-size="22" fill="var(--charcoal)">SAVE 50% OFF</text>
        <text x="199" y="120" text-anchor="middle" font-family="Lato, sans-serif" font-size="11" fill="#444">Vexolith, Floor Plans</text>
        <text x="199" y="133" text-anchor="middle" font-family="Lato, sans-serif" font-size="11" fill="#444">&amp; Photography</text>
      </g>
    </svg>

    <div class="partner"><span class="partner__mark"></span>vexolith</div>

    <div class="footer">
      <svg class="wave" style="top:0" width="411" height="114" viewBox="0 0 411 114">
        <path d="M0,50 Q205,-14 411,50 L411,58 Q205,-4 0,58 Z" fill="var(--gold)"/>
        <path d="M0,63 Q205,3 411,63 L411,114 L0,114 Z" fill="var(--charcoal)"/>
      </svg>
      <div class="footer__call">CALL TODAY
        <svg width="26" height="26" viewBox="0 0 26 26"><circle cx="13" cy="13" r="11.5" fill="none" stroke="var(--gold)" stroke-width="1.8"/><path d="M9,7.5 L11,7.5 L12,10.5 L10.6,11.6 Q11.8,14.2 14.4,15.4 L15.5,14 L18.5,15 L18.5,17 Q18.5,18.5 17,18.5 Q8,18 7.5,9 Q7.5,7.5 9,7.5 Z" fill="var(--gold)"/></svg>
        <span class="footer__phone">778.514.0962</span></div>
      <div class="footer__contact">
        <svg width="10" height="8" viewBox="0 0 10 8"><rect x="0.5" y="0.5" width="9" height="7" fill="var(--gold)"/><path d="M0.5,0.5 L5,4.5 L9.5,0.5" fill="none" stroke="var(--charcoal)" stroke-width="1"/></svg>dorian@quillfenstudio.com &nbsp;|&nbsp;
        <svg width="10" height="10" viewBox="0 0 10 10"><circle cx="5" cy="5" r="4.3" fill="none" stroke="var(--gold)" stroke-width="1.2"/><line x1="0.7" y1="5" x2="9.3" y2="5" stroke="var(--gold)"/><ellipse cx="5" cy="5" rx="2" ry="4.3" fill="none" stroke="var(--gold)"/></svg>www.quillfenstudio.com
      </div>
    </div>
  </section>

</div>
</body>
</html>
```